BKT Business Card

Business card design for a handyman company. Want to portray a professional image and stay away from the "Mom & Pops" image that is normally associated with handyman companies.

```html
<!DOCTYPE html>
<html lang="en">
<head>
<meta charset="utf-8">
<title>BKT Business Card</title>
<link href="https://fonts.googleapis.com/css2?family=Mulish:wght@400;600;800&display=swap" rel="stylesheet">
<style>
  :root {
    --navy: #0a1d37;
    --white: #ffffff;
    --backdrop: #e8e8e8;
    --card-shadow: rgba(0,0,0,0.08);
  }
  * { margin: 0; padding: 0; box-sizing: border-box; }
  html, body { width: 1200px; height: 1000px; overflow: hidden; }
  body {
    background: var(--backdrop);
    font-family: "Mulish", Arial, sans-serif;
    position: relative;
  }
  .card {
    position: absolute;
    top: 350px;
    width: 517px;
    height: 303px;
    background: var(--white);
    overflow: hidden;
    box-shadow: 0 1px 3px var(--card-shadow);
  }
  .card--front { left: 72px; }
  .card--back { left: 622px; }

  .brand {
    position: absolute;
    display: flex;
    align-items: center;
    gap: 10px;
    color: var(--navy);
    font-weight: 800;
    letter-spacing: 2px;
    line-height: 1;
  }
  .brand__mark {
    width: 14px;
    height: 14px;
    background: var(--navy);
  }
  .card--front .brand { left: 28px; top: 36px; font-size: 58px; }
  .card--back .brand { left: 50%; top: 96px; transform: translateX(-50%); font-size: 64px; }

  .front__band {
    position: absolute;
    left: 0; top: 133px;
    width: 100%; height: 170px;
    background: var(--navy);
  }
  .tagline {
    color: var(--white);
    font-weight: 800;
    font-size: 14px;
    letter-spacing: -0.2px;
    white-space: nowrap;
  }
  .front__band .tagline { position: absolute; left: 26px; top: 13px; }

  .contact {
    position: absolute;
    left: 26px; top: 40px;
    list-style: none;
    color: var(--white);
    font-size: 14px;
  }
  .contact li {
    display: flex;
    align-items: center;
    gap: 9px;
    height: 26px;
  }
  .contact svg { width: 16px; height: 14px; fill: var(--white); flex: none; }

  .services {
    position: absolute;
    left: 328px; top: 62px;
    width: 169px; height: 182px;
    background: var(--white);
    border-radius: 20px;
    padding: 2px 3px 3px 2px;
  }
  .services__inner {
    width: 100%; height: 100%;
    background: var(--navy);
    border-radius: 18px;
    padding: 20px 0 0 15px;
    color: var(--white);
  }
  .services__title { font-size: 16px; font-weight: 600; margin-bottom: 5px; }
  .services__list { list-style: none; font-size: 14px; }
  .services__list li {
    display: flex; align-items: center; gap: 6px; height: 22px;
  }
  .services__list li::before {
    content: ""; width: 7px; height: 7px; background: var(--white);
  }

  .back__bar {
    position: absolute;
    top: 131px; height: 41px;
    width: 91px;
    background: var(--navy);
  }
  .back__bar--left { left: 0; }
  .back__bar--right { right: 0; width: 92px; }
  .card--back .tagline {
    position: absolute;
    top: 188px; left: 0; width: 100%;
    text-align: center;
    color: var(--navy);
    font-size: 15px;
  }
</style>
</head>
<body>

<section class="card card--front">
  <div class="brand"><span class="brand__mark"></span>BKT</div>
  <div class="front__band">
    <p class="tagline">RESIDENTIAL &amp; COMMERCIAL SERVICES</p>
    <ul class="contact">
      <li>
        <svg viewBox="0 0 16 14" aria-hidden="true"><path d="M1 5 Q8 0 15 5 L13 7 L11 5.5 L11 4 Q8 3 5 4 L5 5.5 L3 7 Z"/><path d="M4 8 L6 6 L10 6 L12 8 L12 12 L4 12 Z"/></svg>
        (785) 555-0147
      </li>
      <li>
        <svg viewBox="0 0 16 14" aria-hidden="true"><rect x="4" y="1" width="8" height="4"/><rect x="1" y="5" width="14" height="6" rx="1"/><rect x="4" y="9" width="8" height="4" fill="#0a1d37" stroke="#fff" stroke-width="1.4"/></svg>
        (785) 555-0183
      </li>
      <li>
        <svg viewBox="0 0 16 14" aria-hidden="true"><rect x="1" y="3" width="14" height="9"/><path d="M1 3 L8 8 L15 3" fill="none" stroke="#0a1d37" stroke-width="1.4"/></svg>
        info@BKTHomeCare.com
      </li>
      <li class="contact__address">410 Elm Ridge Rd Salina, Ks 67401</li>
    </ul>
  </div>
  <aside class="services">
    <div class="services__inner">
      <p class="services__title">Potential Verbage</p>
      <ul class="services__list">
        <li>Home Repairs</li>
        <li>Handyman</li>
        <li>Services</li>
        <li>Drain Cleaning</li>
        <li>Carpet Cleaning</li>
      </ul>
    </div>
  </aside>
</section>

<section class="card card--back">
  <div class="back__bar back__bar--left"></div>
  <div class="back__bar back__bar--right"></div>
  <div class="brand"><span class="brand__mark"></span>BKT</div>
  <p class="tagline">RESIDENTIAL &amp; COMMERCIAL SERVICES</p>
</section>

</body>
</html>
```